Elegant Tavaroa Rhum Label Design-

We are creating a Rum Distillery in the paradise island of Bora Bora which is a beautiful and exclusive honeymoon and tourist destination in the South Pacific. Our Rum label needs to reflect the beauty of Bora Bora and French Polynesia.
We would like to see designs that include the image of Mount Otemanu (* the mountain of Bora Bora) with an overwater bungalow in the image with the lagoon. We would like the label to have a turquoise color theme with either silver, white, or gold as the outline of the images. We are also open to some tropical colors as well that represent this paradise. The image needs to represent high quality class. The bottle will be sold mostly to tourist at a premium price.

On the label it needs to have Tavaroa Rhum as the main name-
Subheader- Light Rhum
Sub Sub header- Distilled and Bottled in Bora Bora
It needs to have 40% vol and 70cl on the label

Target Market(s)

American tourists in Bora Bora, French Polynesia

Industry/Entity Type

Rum Distillery

Colors
0094D4
00A9DD
6FCCEA
C7EBF8
E9F6FB
00AB8E
00BBA5
67D7C9
C6EFE9
E9F9F6

Requirements
Must have
• The mountain image of Otemanu and an overwater bungalow which is symbolic of Bora Bora.

```html
<!DOCTYPE html>
<html lang="en">
<head>
<meta charset="utf-8">
<title>Tavaroa Rhum – Label Variants</title>
<link rel="stylesheet" href="https://fonts.googleapis.com/css2?family=Sancreek&family=Libre+Baskerville:wght@700&display=swap">
<style>
  :root {
    --page: #ffffff;
    --label-ink: #0d0713;
    --gold: #d08a2a;
    --gold-dark: #7a4a12;
    --title-red: #c0223a;
    --title-edge: #f4efe8;
    --ribbon: #e8e4df;
    --text-dark: #111111;
    --text-light: #f2f2f2;
    --sky: #1aa7d3;
    --cloud: #e9f6fb;
    --peak-green: #4d8f5c;
    --peak-blue: #2f7fa8;
    --lagoon: #2cc3d0;
    --lagoon-deep: #00a9dd;
  }
  html, body {
    margin: 0;
    width: 1200px;
    height: 1200px;
    overflow: hidden;
    background: var(--page);
  }
  .canvas {
    position: relative;
    width: 1200px;
    height: 1200px;
  }
  .label {
    position: absolute;
    width: 486px;
    height: 578px;
  }
  .label--classic { left: 70px; top: 289px; }
  .label--ornate { left: 603px; top: 292px; }
  .label-title {
    font-family: "Sancreek", "Georgia", serif;
    fill: var(--title-red);
    stroke: var(--title-edge);
    stroke-width: 5px;
    paint-order: stroke;
  }
  .label-sub {
    fill: var(--text-dark);
  }
  .label-sub--serif {
    font-family: "Libre Baskerville", "Georgia", serif;
    font-weight: 700;
  }
  .label-sub--display {
    font-family: "Sancreek", "Georgia", serif;
    stroke: var(--ribbon);
    stroke-width: 2px;
    paint-order: stroke;
  }
  .ribbon-text {
    font-family: "Libre Baskerville", "Georgia", serif;
    font-weight: 700;
    fill: var(--text-dark);
  }
  .spec {
    font-family: "Libre Baskerville", "Georgia", serif;
    font-weight: 700;
    fill: var(--text-light);
  }
</style>
</head>
<body>
<main class="canvas">

  <!-- Variant A: serif sub-header, darker mountain -->
  <svg class="label label--classic" viewBox="0 0 810 963" xmlns="http://www.w3.org/2000/svg">
    <defs>
      <linearGradient id="scene-a" x1="0" y1="0" x2="0" y2="1">
        <stop offset="0" stop-color="var(--sky)"/>
        <stop offset="0.22" stop-color="var(--cloud)"/>
        <stop offset="0.38" stop-color="#1d2a22"/>
        <stop offset="0.5" stop-color="var(--peak-green)"/>
        <stop offset="0.58" stop-color="var(--lagoon)"/>
        <stop offset="1" stop-color="var(--lagoon-deep)"/>
      </linearGradient>
      <radialGradient id="flourish-a" cx="0.5" cy="0.5" r="0.5">
        <stop offset="0" stop-color="var(--gold)" stop-opacity="0.75"/>
        <stop offset="1" stop-color="var(--gold)" stop-opacity="0"/>
      </radialGradient>
    </defs>
    <rect class="label-ground" width="810" height="963" fill="var(--label-ink)"/>
    <rect class="border-outer" x="14" y="14" width="782" height="935" fill="none" stroke="var(--gold)" stroke-width="4"/>
    <rect class="border-inner" x="24" y="24" width="762" height="915" fill="none" stroke="var(--gold-dark)" stroke-width="2"/>

    <g class="corner-flourishes">
      <rect role="img" aria-label="Gold scroll ornament, top left" x="30" y="30" width="170" height="130" fill="url(#flourish-a)"/>
      <rect role="img" aria-label="Gold scroll ornament, top right" x="610" y="30" width="170" height="130" fill="url(#flourish-a)"/>
      <rect role="img" aria-label="Gold scroll ornament, bottom left" x="30" y="805" width="170" height="130" fill="url(#flourish-a)"/>
      <rect role="img" aria-label="Gold scroll ornament, bottom right" x="610" y="805" width="170" height="130" fill="url(#flourish-a)"/>
    </g>

    <path class="cartouche-scene" role="img"
      aria-label="Illustration of Mount Otemanu above the lagoon, with palm trees and overwater bungalows on stilts"
      d="M120 130 Q405 30 690 130 Q720 190 770 200 L770 780 Q720 790 690 840 Q560 930 405 925 Q250 930 120 840 Q90 790 40 780 L40 200 Q90 190 120 130 Z"
      fill="url(#scene-a)"/>
    <path class="cartouche-frame"
      d="M120 130 Q405 30 690 130 Q720 190 770 200 L770 780 Q720 790 690 840 Q560 930 405 925 Q250 930 120 840 Q90 790 40 780 L40 200 Q90 190 120 130 Z"
      fill="none" stroke="var(--gold)" stroke-width="7"/>

    <text class="label-title" x="405" y="395" text-anchor="middle" font-size="130">Tavaroa</text>
    <text class="label-title" x="405" y="560" text-anchor="middle" font-size="140">Rhum</text>

    <text class="label-sub label-sub--serif" x="432" y="655" text-anchor="middle" font-size="44">LIGHT RHUM</text>

    <g class="ribbon">
      <path d="M48 652 C200 612 300 745 420 745 C540 745 650 640 762 612 L770 668 C655 698 545 805 420 805 C295 805 200 675 58 712 Z"
        fill="var(--ribbon)" stroke="var(--gold)" stroke-width="4"/>
      <path id="ribbon-line-a" d="M70 670 C210 640 300 770 420 770 C540 770 650 670 760 640" fill="none"/>
      <text class="ribbon-text" font-size="29"><textPath href="#ribbon-line-a" startOffset="50%" text-anchor="middle">DISTILLED AND BOTTLED IN BORA BORA</textPath></text>
    </g>

    <text class="spec" x="186" y="860" text-anchor="middle" font-size="30">40%</text>
    <text class="spec" x="186" y="890" text-anchor="middle" font-size="25">alc/vol</text>
    <text class="spec" x="628" y="872" text-anchor="middle" font-size="40">70<tspan font-size="30">CL</tspan></text>
  </svg>

  <!-- Variant B: display sub-header, blue mountain -->
  <svg class="label label--ornate" viewBox="0 0 810 963" xmlns="http://www.w3.org/2000/svg">
    <defs>
      <linearGradient id="scene-b" x1="0" y1="0" x2="0" y2="1">
        <stop offset="0" stop-color="var(--sky)"/>
        <stop offset="0.22" stop-color="var(--cloud)"/>
        <stop offset="0.38" stop-color="var(--peak-blue)"/>
        <stop offset="0.5" stop-color="var(--peak-green)"/>
        <stop offset="0.58" stop-color="var(--lagoon)"/>
        <stop offset="1" stop-color="var(--lagoon-deep)"/>
      </linearGradient>
      <radialGradient id="flourish-b" cx="0.5" cy="0.5" r="0.5">
        <stop offset="0" stop-color="var(--gold)" stop-opacity="0.75"/>
        <stop offset="1" stop-color="var(--gold)" stop-opacity="0"/>
      </radialGradient>
    </defs>
    <rect class="label-ground" width="810" height="963" fill="var(--label-ink)"/>
    <rect class="border-outer" x="14" y="14" width="782" height="935" fill="none" stroke="var(--gold)" stroke-width="4"/>
    <rect class="border-inner" x="24" y="24" width="762" height="915" fill="none" stroke="var(--gold-dark)" stroke-width="2"/>

    <g class="corner-flourishes">
      <rect role="img" aria-label="Gold scroll ornament, top left" x="30" y="30" width="170" height="130" fill="url(#flourish-b)"/>
      <rect role="img" aria-label="Gold scroll ornament, top right" x="610" y="30" width="170" height="130" fill="url(#flourish-b)"/>
      <rect role="img" aria-label="Gold scroll ornament, bottom left" x="30" y="805" width="170" height="130" fill="url(#flourish-b)"/>
      <rect role="img" aria-label="Gold scroll ornament, bottom right" x="610" y="805" width="170" height="130" fill="url(#flourish-b)"/>
    </g>

    <path class="cartouche-scene" role="img"
      aria-label="Illustration of a blue-green Mount Otemanu above the turquoise lagoon, with palm trees and overwater bungalows"
      d="M120 130 Q405 30 690 130 Q720 190 770 200 L770 780 Q720 790 690 840 Q560 930 405 925 Q250 930 120 840 Q90 790 40 780 L40 200 Q90 190 120 130 Z"
      fill="url(#scene-b)"/>
    <path class="cartouche-frame"
      d="M120 130 Q405 30 690 130 Q720 190 770 200 L770 780 Q720 790 690 840 Q560 930 405 925 Q250 930 120 840 Q90 790 40 780 L40 200 Q90 190 120 130 Z"
      fill="none" stroke="var(--gold)" stroke-width="7"/>

    <text class="label-title" x="405" y="395" text-anchor="middle" font-size="130">Tavaroa</text>
    <text class="label-title" x="405" y="560" text-anchor="middle" font-size="140">Rhum</text>

    <text class="label-sub label-sub--display" x="425" y="660" text-anchor="middle" font-size="50">LIGHT RHUM</text>

    <g class="ribbon">
      <path d="M48 652 C200 612 300 745 420 745 C540 745 650 640 762 612 L770 668 C655 698 545 805 420 805 C295 805 200 675 58 712 Z"
        fill="var(--ribbon)" stroke="var(--gold)" stroke-width="4"/>
      <path id="ribbon-line-b" d="M70 670 C210 640 300 770 420 770 C540 770 650 670 760 640" fill="none"/>
      <text class="ribbon-text" font-size="29"><textPath href="#ribbon-line-b" startOffset="50%" text-anchor="middle">DISTILLED AND BOTTLED IN BORA BORA</textPath></text>
    </g>

    <text class="spec" x="186" y="860" text-anchor="middle" font-size="30">40%</text>
    <text class="spec" x="186" y="890" text-anchor="middle" font-size="25">alc/vol</text>
    <text class="spec" x="628" y="872" text-anchor="middle" font-size="40">70<tspan font-size="30">CL</tspan></text>
  </svg>

</main>
</body>
</html>
```